Business Card - Cooperate

Business Card for Larkfield Management Consulting

Target Market(s)

Corparte - b2B

Industry/Entity Type

Management Consulting - Professional Services

Contact Information for Business Card

Company Name , Slogan , Dummy Address,

Requirements
Must have
• Reach your Full Potential

```html
<!DOCTYPE html>
<html lang="en">
<head>
<meta charset="utf-8">
<title>Larkfield Management Consulting – Business Card</title>
<link href="https://fonts.googleapis.com/css2?family=Montserrat:wght@500;600;700;800&display=swap" rel="stylesheet">
<style>
  :root {
    --backdrop: #c9cacc;
    --card-white: #ffffff;
    --navy: #1f3596;
    --blue: #1c6fcf;
    --green: #2fae4c;
    --teal: #2bb673;
    --ink: #2a2f45;
    --shadow: rgba(0, 0, 0, 0.22);
  }
  * { box-sizing: border-box; margin: 0; padding: 0; }
  html, body {
    width: 900px;
    height: 1200px;
    overflow: hidden;
    background: var(--backdrop);
    font-family: "Montserrat", Arial, sans-serif;
  }
  .canvas {
    position: relative;
    width: 900px;
    height: 1200px;
  }
  .card {
    position: absolute;
    left: 120px;
    width: 660px;
    height: 390px;
    border-radius: 24px;
    box-shadow: 0 8px 18px var(--shadow);
    overflow: hidden;
  }
  .card-front {
    top: 186px;
    background: linear-gradient(180deg, var(--navy) 0%, var(--blue) 55%, var(--green) 92%);
    display: flex;
    align-items: center;
    justify-content: center;
  }
  .card-back {
    top: 660px;
    height: 405px;
    background: var(--card-white);
  }
  .brand {
    display: flex;
    align-items: center;
    gap: 18px;
  }
  .brand-dot {
    border-radius: 50%;
    flex: none;
  }
  .brand-name {
    font-weight: 700;
    line-height: 1;
    letter-spacing: 1px;
  }
  .brand-tagline {
    font-weight: 700;
    text-transform: uppercase;
    letter-spacing: 1.5px;
    color: var(--green);
  }
  .card-front .brand-dot {
    width: 70px;
    height: 70px;
    background: var(--card-white);
  }
  .card-front .brand-name {
    font-size: 76px;
    color: var(--card-white);
  }
  .card-front .brand-tagline {
    font-size: 15px;
    margin-top: 8px;
    color: #7fe08f;
  }
  .card-back .brand {
    position: absolute;
    left: 42px;
    top: 52px;
    gap: 12px;
  }
  .card-back .brand-dot {
    width: 48px;
    height: 48px;
    background: var(--blue);
  }
  .card-back .brand-name {
    font-size: 50px;
    color: var(--navy);
  }
  .card-back .brand-tagline {
    font-size: 10px;
    margin-top: 6px;
  }
  .person {
    position: absolute;
    left: 42px;
    top: 216px;
  }
  .person-name {
    font-size: 36px;
    font-weight: 700;
    color: var(--navy);
  }
  .person-role {
    font-size: 14px;
    font-weight: 700;
    color: var(--green);
    margin-top: 4px;
  }
  .contact-list {
    position: absolute;
    left: 42px;
    top: 300px;
    list-style: none;
  }
  .contact-item {
    display: flex;
    align-items: center;
    gap: 12px;
    font-size: 17px;
    font-weight: 600;
    color: var(--ink);
    height: 30px;
  }
  .contact-icon {
    width: 16px;
    height: 16px;
    fill: var(--green);
    flex: none;
  }
</style>
</head>
<body>
<main class="canvas">
  <section class="card card-front" aria-label="Card front">
    <div class="brand">
      <span class="brand-dot"></span>
      <div>
        <div class="brand-name">larkfield</div>
        <div class="brand-tagline">Reach your full potential</div>
      </div>
    </div>
  </section>

  <section class="card card-back" aria-label="Card back">
    <div class="brand">
      <span class="brand-dot"></span>
      <div>
        <div class="brand-name">larkfield</div>
        <div class="brand-tagline">Reach your full potential</div>
      </div>
    </div>

    <div class="person">
      <div class="person-name">Daniel Hart</div>
      <div class="person-role">CEO</div>
    </div>

    <ul class="contact-list">
      <li class="contact-item">
        <svg class="contact-icon" viewBox="0 0 24 24" aria-hidden="true"><path d="M6.6 10.8a15.2 15.2 0 0 0 6.6 6.6l2.2-2.2a1 1 0 0 1 1-.25 11.4 11.4 0 0 0 3.6.57 1 1 0 0 1 1 1V20a1 1 0 0 1-1 1A17 17 0 0 1 3 4a1 1 0 0 1 1-1h3.5a1 1 0 0 1 1 1c0 1.25.2 2.46.57 3.6a1 1 0 0 1-.25 1z"/></svg>
        (555) 014-2290
      </li>
      <li class="contact-item">
        <svg class="contact-icon" viewBox="0 0 24 24" aria-hidden="true"><path d="M2 5h20v14H2zm2 2v.5l8 5 8-5V7zm0 2.9V17h16V9.9l-8 5z"/></svg>
        info@larkfield.com
      </li>
      <li class="contact-item">
        <svg class="contact-icon" viewBox="0 0 24 24" aria-hidden="true"><path d="M12 2a10 10 0 1 0 0 20 10 10 0 0 0 0-20zm6.9 6h-3a15.6 15.6 0 0 0-1.4-3.6A8 8 0 0 1 18.9 8zM12 4c.8 1.2 1.5 2.5 1.9 4h-3.8c.4-1.5 1.1-2.8 1.9-4zM4.3 14a8 8 0 0 1 0-4h3.4a16 16 0 0 0 0 4zm.8 2h3a15.6 15.6 0 0 0 1.4 3.6A8 8 0 0 1 5.1 16zm3-8h-3a8 8 0 0 1 4.4-3.6A15.6 15.6 0 0 0 8.1 8zM12 20c-.8-1.2-1.5-2.5-1.9-4h3.8c-.4 1.5-1.1 2.8-1.9 4zm2.3-6H9.7a14.6 14.6 0 0 1 0-4h4.6a14.6 14.6 0 0 1 0 4zm.2 5.6a15.6 15.6 0 0 0 1.4-3.6h3a8 8 0 0 1-4.4 3.6zm1.8-5.6a16 16 0 0 0 0-4h3.4a8 8 0 0 1 0 4z"/></svg>
        www.larkfield.com
      </li>
    </ul>
  </section>
</main>
</body>
</html>
```